Simple proffessional BC

I have a logo which I will attach below.
I would like the logo on the front of the card with these details in point form below:
Pre and Post Natal Yoga: Pregnancy Workshops: Hypnobirthing Courses
On the back of the card my details:
Marla Penrick
Facebook page- calmcradlestudiolakebay
Mobile- 0482 315 746

I like the idea of the card being simple, possibly just the above on a plain coloured (eggshell?) card, a card that is textured.
I am open to suggestion if it appeals!
Thank you and good luck!

Target Market(s)

Pregnant women, 20's-40's

Requirements
Must have
• Simple, compliment logo.
Make logo the feature.
Should not have

```html
<!DOCTYPE html>
<html lang="en">
<head>
<meta charset="utf-8">
<title>Calm Cradle – Business Card</title>
<link rel="stylesheet" href="https://fonts.googleapis.com/css2?family=Courgette&display=swap">
<style>
  :root {
    --backdrop: #e4e4e4;
    --card-top: #fefbdc;
    --card-bottom: #f9f3bf;
    --band: #fefce9;
    --ink: #1d1a14;
    --shadow: rgba(0, 0, 0, 0.18);
  }
  * { box-sizing: border-box; margin: 0; padding: 0; }
  html, body {
    width: 1000px;
    height: 1200px;
    overflow: hidden;
    background: var(--backdrop);
  }
  .canvas {
    position: relative;
    width: 1000px;
    height: 1200px;
  }
  .card {
    position: absolute;
    left: 100px;
    width: 800px;
    height: 457px;
    background: linear-gradient(180deg, var(--card-top) 0%, var(--card-bottom) 100%);
    box-shadow: 0 8px 22px var(--shadow);
    overflow: hidden;
  }
  .card--front { top: 90px; }
  .card--back { top: 653px; }

  .brand-band {
    position: absolute;
    left: 64px;
    top: 0;
    width: 104px;
    height: 100%;
    background: var(--band);
  }
  .brand-name {
    position: absolute;
    left: 64px;
    bottom: 40px;
    width: 104px;
    text-align: center;
    font-family: "Courgette", cursive;
    font-size: 25px;
    line-height: 34px;
    color: var(--ink);
  }

  .services {
    position: absolute;
    left: 440px;
    top: 300px;
    list-style: none;
    font-family: "Courgette", cursive;
    font-size: 25px;
    line-height: 42px;
    color: var(--ink);
  }

  .contact {
    position: absolute;
    left: 66px;
    top: 300px;
    font-family: "Courgette", cursive;
    color: var(--ink);
  }
  .contact__name {
    font-size: 30px;
    line-height: 44px;
  }
  .contact__line {
    font-size: 23px;
    line-height: 34px;
  }
</style>
</head>
<body>
<main class="canvas">
  <section class="card card--front" aria-label="Card front">
    <div class="brand-band"></div>
    <p class="brand-name">Calm<br>Cradle</p>
    <ul class="services">
      <li>Pre and Post Natal Yoga</li>
      <li>Pregnancy Workshops</li>
      <li>Hypnobirthing Courses</li>
    </ul>
  </section>

  <section class="card card--back" aria-label="Card back">
    <div class="contact">
      <p class="contact__name">Marla Penrick</p>
      <p class="contact__line">Fb: calmcradlestudiolakebay</p>
      <p class="contact__line">0482 315 746</p>
    </div>
  </section>
</main>
</body>
</html>
```